Dental Office Needs a Flyer Design to Attract New Patients

We need a flyer design for a dental office in Rockville, MD, US. Our office name is Brightpeak Dental Care. Our website is: brightpeakdentalcare.example and our office logo can be seen on the website. We would like stay that call and make an appointment with Dr. Le Ko. The flyer can follow the color scheme of our logo (blue and white). We current have Holiday/New Year special: Dental exam, x-ray, and cleaning for $95 (a $300 value); please include this in the flyer. Also if you can include a winter inspired picture to be part of the flyer, that would be great. We really like your Grin Tallowa flyer design and are looking for something similar. Thank you!
Target Market(s)
Apartment complex that is 5 minutes (less than 1 mile away)
Industry/Entity Type
Dental
Look and feel

```html
<!DOCTYPE html>
<html lang="en">
<head>
<meta charset="utf-8">
<title>Brightpeak Dental Care – Holiday/New Year Special Offer</title>
<link href="https://fonts.googleapis.com/css2?family=Roboto+Condensed:wght@300;400;700&display=swap" rel="stylesheet">
<style>
  :root {
    --brand-blue: #2b3f94;
    --ink: #222a33;
    --accent-green: #8ab52a;
    --bullet-green: #7fb02a;
    --emergency-red: #d62a27;
    --pale-sky: #cde6ea;
    --pale-mist: #f4fafb;
    --footer-dark: #333437;
    --page-bg: #e6e7e9;
    --white: #ffffff;
  }
  * { box-sizing: border-box; margin: 0; padding: 0; }
  html, body { width: 1200px; height: 1200px; overflow: hidden; background: var(--page-bg); }
  body { font-family: "Roboto Condensed", Arial, sans-serif; color: var(--ink); }

  .flyer {
    position: absolute; left: 200px; top: 35px;
    width: 800px; height: 1130px; overflow: hidden;
    background: radial-gradient(ellipse at 45% 62%, var(--pale-mist) 0%, #e6f2f4 45%, var(--pale-sky) 100%);
    box-shadow: 0 4px 14px rgba(0,0,0,.25);
  }
  .flyer-shapes { position: absolute; inset: 0; }

  .winter-photo {
    position: absolute; inset: 0;
    clip-path: polygon(0 118px, 609px 0, 800px 0, 800px 402px, 0 532px);
    background: linear-gradient(160deg, #e9edf0 0%, #c9c3bb 35%, #9e8f80 55%, #d7dde4 80%, #f1f3f5 100%);
  }

  .top-band-title {
    position: absolute; left: 28px; top: 70px;
    transform: rotate(-11.4deg); transform-origin: left bottom;
    color: var(--white); font-size: 19px; font-weight: 300; letter-spacing: .3px;
    white-space: nowrap;
  }
  .top-band-title strong { font-weight: 700; font-size: 21px; }

  .photo-circle {
    position: absolute; width: 208px; height: 208px; border-radius: 50%;
    border: 8px solid var(--white);
    box-shadow: 0 3px 8px rgba(0,0,0,.18);
  }
  .photo-circle.patient-exam { left: 41px; top: 411px; background: radial-gradient(circle at 40% 45%, #e9c3a8, #c9d6df 70%, #f1f2f4); }
  .photo-circle.friends-smiling { left: 297px; top: 367px; background: radial-gradient(circle at 50% 45%, #efcdb3, #a88a6e 60%, #e8e9ec); }
  .photo-circle.dental-checkup { left: 553px; top: 329px; background: radial-gradient(circle at 45% 55%, #eac7ae, #9a7350 55%, #dfe6ea); }

  .offer-box {
    position: absolute; left: 468px; top: 578px; width: 332px; height: 167px;
    background: var(--brand-blue); color: var(--white);
    border-radius: 8px 0 0 8px;
    border: 3px solid var(--white); border-right: none;
    box-shadow: 0 4px 8px rgba(0,0,0,.25);
    padding: 20px 0 0 17px;
  }
  .offer-title { font-size: 22px; font-weight: 300; white-space: nowrap; }
  .offer-title strong { font-weight: 700; }
  .offer-details { position: absolute; left: 17px; top: 75px; font-size: 15px; line-height: 20px; }
  .offer-details .offer-value { font-weight: 700; display: block; margin-top: 2px; }
  .offer-price { position: absolute; left: 168px; top: 66px; font-weight: 700; line-height: 1; }
  .offer-price .currency { font-size: 34px; vertical-align: top; position: relative; top: 4px; }
  .offer-price .amount { font-size: 72px; letter-spacing: -2px; }

  .service-list { position: absolute; top: 655px; }
  .service-list.treatments { left: 59px; }
  .service-list.services { left: 281px; }
  .service-list h3 {
    font-size: 15px; font-weight: 700; color: var(--ink);
    text-decoration: underline; text-underline-offset: 2px; margin-bottom: 3px;
  }
  .service-list ul { list-style: none; }
  .service-list li {
    font-size: 14.5px; line-height: 19.2px; font-weight: 400; color: var(--ink);
    padding-left: 18px; position: relative; white-space: nowrap;
  }
  .service-list li::before {
    content: ""; position: absolute; left: 1px; top: 5px;
    width: 10px; height: 10px; border-radius: 50%; background: var(--bullet-green);
  }

  .emergency { position: absolute; left: 506px; top: 783px; width: 200px; text-align: center; }
  .emergency-mark { display: block; margin: 0 auto; }
  .emergency-label { font-size: 17px; font-weight: 400; margin-top: 2px; }

  .dentist { position: absolute; left: 59px; top: 893px; }
  .dentist-name { font-size: 31px; font-weight: 700; color: var(--brand-blue); letter-spacing: -.3px; }
  .dentist-title { font-size: 17px; font-weight: 400; letter-spacing: 1.6px; margin-top: -1px; }

  .booking { position: absolute; left: 446px; top: 897px; width: 320px; text-align: center; }
  .booking-line { font-size: 22px; font-weight: 700; color: var(--ink); }
  .booking-phone { font-size: 30px; font-weight: 700; color: var(--accent-green); margin-top: 1px; }

  .brand-name {
    position: absolute; left: 51px; top: 1040px;
    display: flex; align-items: center; gap: 7px;
    font-size: 19px; font-weight: 700; color: var(--brand-blue); white-space: nowrap;
  }
  .brand-name .brand-dot { width: 14px; height: 14px; border-radius: 50%; background: var(--brand-blue); }

  .footer-contact { position: absolute; left: 334px; top: 1055px; color: var(--white); font-size: 15px; }
  .footer-contact .row { display: flex; align-items: center; gap: 10px; height: 25px; white-space: nowrap; }
  .footer-divider { position: absolute; left: 604px; top: 1050px; width: 2px; height: 55px; background: var(--white); }
  .footer-address { position: absolute; left: 622px; top: 1060px; color: var(--white); font-size: 15px; line-height: 20px; font-style: normal; }
</style>
</head>
<body>
<main class="flyer">
  <div class="winter-photo" role="img" aria-label="Photo of a smiling family sledding together in a snowy winter forest"></div>

  <svg class="flyer-shapes" width="800" height="1130" viewBox="0 0 800 1130" aria-hidden="true">
    <polygon points="0,0 612,0 0,119" fill="var(--brand-blue)"/>
    <path d="M220,1130 L305,1040 Q318,1027 336,1027 L800,1027 L800,1130 Z" fill="var(--footer-dark)"/>
  </svg>

  <p class="top-band-title">HOLIDAY/NEW YEAR <strong>SPECIAL OFFER!</strong></p>

  <div class="photo-circle patient-exam" role="img" aria-label="Photo of a woman having a dental exam"></div>
  <div class="photo-circle friends-smiling" role="img" aria-label="Photo of two young women smiling"></div>
  <div class="photo-circle dental-checkup" role="img" aria-label="Photo of a patient during a dental check-up"></div>

  <section class="offer-box">
    <h2 class="offer-title">Holiday/New Year <strong>Special Offer!</strong></h2>
    <p class="offer-details">DENTAL EXAM, X-RAY<br>AND CLEANING FOR<span class="offer-value">(COST $300)</span></p>
    <p class="offer-price"><span class="currency">$</span><span class="amount">95</span></p>
  </section>

  <section class="service-list treatments">
    <h3>DENTAL TREATMENTS</h3>
    <ul>
      <li>6 Months Maitenance</li>
      <li>Cosmetic Dentistry</li>
      <li>Crowns and Bridges</li>
      <li>Dental Implants</li>
      <li>Fissure Sealents</li>
      <li>Clear Aligners</li>
      <li>Periodontal Treatment</li>
      <li>Root Canal Treatment</li>
      <li>Tooth Coloured Fillings</li>
      <li>Tooth Replacement</li>
    </ul>
  </section>

  <section class="service-list services">
    <h3>OUR SERVICES</h3>
    <ul>
      <li>Preventive Dentistry</li>
      <li>Cosmetic Dentistry</li>
      <li>Tooth Replacement</li>
      <li>Endodontics</li>
      <li>Clear Aligners</li>
    </ul>
  </section>

  <section class="emergency">
    <svg class="emergency-mark" width="140" height="70" viewBox="0 0 140 70" aria-hidden="true">
      <path d="M40,58 Q70,74 104,60 Q130,44 120,20 Q110,2 84,4" fill="none" stroke="var(--accent-green)" stroke-width="4" stroke-linecap="round"/>
      <g stroke="var(--accent-green)" stroke-width="1.5">
        <line x1="98" y1="10" x2="95" y2="15"/><line x1="110" y1="20" x2="105" y2="23"/><line x1="116" y1="34" x2="110" y2="35"/><line x1="112" y1="48" x2="107" y2="46"/>
      </g>
      <text x="8" y="47" font-family="Roboto Condensed, Arial, sans-serif" font-weight="700" font-size="30" fill="var(--emergency-red)" letter-spacing="1">24/7</text>
    </svg>
    <p class="emergency-label">Emergency Dental Services</p>
  </section>

  <section class="dentist">
    <h1 class="dentist-name">Le Minh Ko, D.D.S</h1>
    <p class="dentist-title">General &amp; Cosmetic Dentist</p>
  </section>

  <section class="booking">
    <p class="booking-line">Book Your Appointment Today!</p>
    <p class="booking-phone">Call 301-555-0148</p>
  </section>

  <div class="brand-name"><span class="brand-dot"></span>Brightpeak Dental Care</div>

  <div class="footer-contact">
    <div class="row">
      <svg width="16" height="16" viewBox="0 0 16 16" aria-hidden="true"><rect x="1" y="1" width="14" height="14" rx="2" fill="none" stroke="#fff" stroke-width="1.3"/><path d="M6,4 Q4,8 6,12 L8,11 L7,9 Q6.5,8 7,7 L8,5 Z" fill="#fff"/></svg>
      <span>301-555-0148</span>
    </div>
    <div class="row">
      <svg width="16" height="16" viewBox="0 0 16 16" aria-hidden="true"><g fill="none" stroke="#fff" stroke-width="1.2"><circle cx="8" cy="8" r="7"/><ellipse cx="8" cy="8" rx="3" ry="7"/><line x1="1" y1="8" x2="15" y2="8"/><line x1="2.5" y1="4.5" x2="13.5" y2="4.5"/><line x1="2.5" y1="11.5" x2="13.5" y2="11.5"/></g></svg>
      <span>www.brightpeakdentalcaremd.example</span>
    </div>
  </div>
  <div class="footer-divider"></div>
  <address class="footer-address">4170 Larkspur Lane<br>Rockville, MD 20852</address>
</main>
</body>
</html>
```